Business Card Design needed for start up company Pelmora

In need of a new business card designed for a start up company based in Sydney, Pelmora is a new start up innovative Company, our mission it to make property accessible for everyday Australian and to become the leading Real Estate platform in Australia. We want it to be fresh and clean.

Industry/Entity Type

Financial

Contact Information for Business Card

Section for Name
Section for Title

PELMORA - Keys Within Reach
Mobile:
Direct:

Font styles to use
Sans Serif

Colors
33a6d7
0692cd
0255a3
ffffff

Requirements
Must have
• Logo, all business card details

```html
<!DOCTYPE html>
<html lang="en">
<head>
<meta charset="utf-8">
<title>Pelmora Business Card</title>
<link rel="stylesheet" href="https://fonts.googleapis.com/css2?family=Open+Sans:wght@400;600;700;800&display=swap">
<style>
  :root {
    --bg: #4a423d;
    --card: #0d0e10;
    --sky: #33a6d7;
    --ocean: #0692cd;
    --navy: #0255a3;
    --white: #ffffff;
  }
  * { margin: 0; padding: 0; box-sizing: border-box; }
  html, body { width: 1200px; height: 844px; overflow: hidden; }
  body {
    background: var(--bg);
    font-family: "Open Sans", Arial, sans-serif;
    display: flex;
    align-items: center;
    justify-content: center;
    gap: 60px;
  }
  .card {
    position: relative;
    width: 500px;
    height: 286px;
    background: var(--card);
    box-shadow: 0 10px 30px rgba(0,0,0,0.45);
  }
  .brand-name {
    position: absolute;
    left: 0;
    right: 0;
    text-align: center;
    font-weight: 800;
    font-size: 50px;
    letter-spacing: -1px;
    color: var(--navy);
    line-height: 1;
  }
  .card-front .brand-name { top: 72px; }
  .card-back .brand-name { top: 96px; }
  .holder { position: absolute; left: 32px; bottom: 34px; }
  .holder-name { color: var(--ocean); font-weight: 600; font-size: 19px; }
  .holder-title { color: var(--white); font-size: 14px; margin-top: 2px; }
  .contact {
    position: absolute;
    right: 26px;
    top: 150px;
    list-style: none;
    text-align: right;
    color: var(--white);
    font-size: 13px;
    line-height: 22px;
  }
  .contact li { display: flex; align-items: center; justify-content: flex-end; gap: 8px; }
  .contact svg { width: 11px; height: 11px; fill: var(--sky); }
  .tagline {
    position: absolute;
    left: 0; right: 0;
    top: 178px;
    text-align: center;
    color: var(--ocean);
    font-weight: 600;
    font-size: 14px;
    letter-spacing: 0.5px;
    text-transform: uppercase;
  }
</style>
</head>
<body>
  <section class="card card-front">
    <p class="brand-name">PELMORA</p>
    <ul class="contact">
      <li>(02)-5550-1842
        <svg viewBox="0 0 12 12"><path d="M2.5 0.5 L4.5 0.5 L5.5 3 L4 4.2 C4.7 5.8 6.2 7.3 7.8 8 L9 6.5 L11.5 7.5 L11.5 9.5 C11.5 10.6 10.6 11.5 9.5 11.5 C4.5 11 1 7.5 0.5 2.5 C0.5 1.4 1.4 0.5 2.5 0.5 Z"/></svg>
      </li>
      <li>0400-555-318
        <svg viewBox="0 0 12 12"><path d="M3 0 H9 A1 1 0 0 1 10 1 V11 A1 1 0 0 1 9 12 H3 A1 1 0 0 1 2 11 V1 A1 1 0 0 1 3 0 Z M3.2 1.5 V9.5 H8.8 V1.5 Z"/></svg>
      </li>
      <li>hello@pelmora.com
        <svg viewBox="0 0 12 12"><path d="M0 2 H12 V10 H0 Z M0.8 2.6 L6 6.6 L11.2 2.6 V3.6 L6 7.6 L0.8 3.6 Z" fill-rule="evenodd"/></svg>
      </li>
    </ul>
    <div class="holder">
      <p class="holder-name">Daniel Hartley</p>
      <p class="holder-title">Managing Director</p>
    </div>
  </section>

  <section class="card card-back">
    <p class="brand-name">PELMORA</p>
    <p class="tagline">Keys Within Reach</p>
  </section>
</body>
</html>
```